Quillmark Hall Business Card

I need a business card design. We are a collaborate online training company. Our colors are gray and green. Our website is QuillmarkHall.com

I would like an area for a profile picture within the card

```html
<!DOCTYPE html>
<html lang="en">
<head>
<meta charset="utf-8">
<title>Quillmark Hall Business Card</title>
<link href="https://fonts.googleapis.com/css2?family=Open+Sans:wght@400;600;700&display=swap" rel="stylesheet">
<style>
  :root {
    --green: #8cc63f;
    --green-deep: #5fa82e;
    --green-light: #a6d65a;
    --ink: #333333;
    --ink-soft: #555555;
    --paper: #ffffff;
    --paper-shade: #eeeeee;
    --page: #e9e7e2;
    --photo-top: #6e6a66;
    --photo-bottom: #3c3a38;
  }
  * { box-sizing: border-box; margin: 0; padding: 0; }
  html, body {
    width: 1200px; height: 843px; overflow: hidden;
    background: var(--page);
    font-family: "Open Sans", Arial, sans-serif;
  }
  .stage {
    position: relative; width: 1200px; height: 843px;
    display: flex; align-items: center; justify-content: center; gap: 50px;
  }
  .card {
    position: relative; width: 540px; height: 308px; overflow: hidden;
    border-radius: 3px;
    box-shadow: 0 6px 18px rgba(0,0,0,0.18);
  }

  /* Front: profile side */
  .card-front {
    background: linear-gradient(135deg, var(--green-light) 0%, var(--green) 45%, var(--green-deep) 100%);
  }
  .profile-photo {
    position: absolute; left: 60px; top: 30px; width: 190px; height: 278px;
    border-radius: 95px 95px 0 0;
    background: linear-gradient(180deg, var(--photo-top), var(--photo-bottom));
  }
  .front-brand {
    position: absolute; right: 34px; top: 120px; text-align: right;
  }
  .front-brand .brand-name {
    font-size: 38px; font-weight: 700; color: var(--ink); letter-spacing: -1px; line-height: 1;
  }
  .front-brand .brand-url {
    margin-top: 6px; font-size: 17px; color: rgba(255,255,255,0.85); letter-spacing: 0.5px;
  }

  /* Back: contact side */
  .card-back {
    background: linear-gradient(180deg, var(--paper) 0%, var(--paper) 60%, var(--paper-shade) 100%);
  }
  .back-band {
    position: absolute; left: 0; right: 0; bottom: 0; height: 26px;
    background: linear-gradient(90deg, var(--green-deep), var(--green));
  }
  .logo-lockup {
    position: absolute; left: 34px; top: 110px; display: flex; align-items: center; gap: 10px;
  }
  .logo-dot { width: 34px; height: 34px; border-radius: 50%; background: var(--green); }
  .logo-name {
    font-size: 28px; font-weight: 700; color: var(--ink); letter-spacing: -0.8px;
  }
  .divider {
    position: absolute; left: 282px; top: 50px; width: 1px; height: 180px;
    background: linear-gradient(180deg, transparent, #c8c8c8 30%, #c8c8c8 70%, transparent);
  }
  .contact {
    position: absolute; left: 304px; top: 56px; color: var(--ink-soft);
    font-size: 14px; line-height: 1.45;
  }
  .contact .person-name { font-size: 21px; font-weight: 600; color: var(--green); line-height: 1.1; }
  .contact .person-role { font-size: 14px; color: var(--ink-soft); margin-bottom: 12px; }
  .contact .line { display: flex; align-items: center; gap: 8px; }
  .contact svg { width: 13px; height: 13px; flex: none; }
</style>
</head>
<body>
<main class="stage">
  <section class="card card-front">
    <div class="profile-photo" role="img" aria-label="Profile photograph of the founder"></div>
    <div class="front-brand">
      <div class="brand-name">Quillmark Hall</div>
      <div class="brand-url">QuillmarkHall.com</div>
    </div>
  </section>

  <section class="card card-back">
    <div class="logo-lockup">
      <span class="logo-dot"></span>
      <span class="logo-name">Quillmark Hall</span>
    </div>
    <div class="divider"></div>
    <div class="contact">
      <div class="person-name">Dana Whitfield</div>
      <div class="person-role">Founder</div>
      <div>480 Larkspur Ave. Suite 7</div>
      <div>Mesa Verde, Oregon 97402</div>
      <div class="line">
        <svg viewBox="0 0 16 16" aria-hidden="true"><path fill="#6db33f" d="M3.5 1.5l2.5 0 1 3.5-1.6 1.2c.8 1.7 2 2.9 3.7 3.7l1.2-1.6 3.5 1v2.5c0 .8-.7 1.5-1.5 1.5C6.8 13.3 2.7 9.2 2 3c0-.8.7-1.5 1.5-1.5z"/></svg>
        <span>(555) 214-0937</span>
      </div>
      <div class="line">
        <svg viewBox="0 0 16 16" aria-hidden="true"><rect x="1" y="3" width="14" height="10" rx="1" fill="#6db33f"/><path d="M1.5 4l6.5 5 6.5-5" fill="none" stroke="#fff" stroke-width="1.3"/></svg>
        <span>dana@quillmarkhall.com</span>
      </div>
      <div class="line">
        <svg viewBox="0 0 16 16" aria-hidden="true"><circle cx="8" cy="8" r="7" fill="#6db33f"/><path d="M1.5 8h13M8 1c-2.5 2.5-2.5 11.5 0 14M8 1c2.5 2.5 2.5 11.5 0 14" fill="none" stroke="#fff" stroke-width="1"/></svg>
        <span>quillmarkhall.com</span>
      </div>
    </div>
    <div class="back-band"></div>
  </section>
</main>
</body>
</html>
```